Brisk Hollow Builders Needs A Flyer

We need a flyer for our newest product "The Cedarlane Garden Workroom"

Here is some copy for the flyer:

1. More and more people everyday are working from home and finding it difficult to disconnect from home activities in order to focus on their work. They are also finding it very expensive to add on to their existing house for a quiet place. Our archatectually stunning, Cedarlane Garden Workroom is the answer. The office studio measures 16' wide and 10' deep. 160 Square feet of space.

Perfect for dozens of purposes. Home office, design studio, artist studio, home school office, reading room, craft studio, drafting room.

Features include:

- Steel Framing. 40-60% lighter then wood, higher strength to weight ratio, resistant to mold and fire and steel is the most recycled material on earth!
- Spray foam insulation. Cool in the summer and warm in the winter.
- HVAC Mini Split with wireless remote control and thermostat.
- 100% Off grid with enough solar and battery storage to run your entire office. No need to pay for an expensive electric installation.
- Flush fitting floor outlets to reduce wires.
- TV mount (Optional with pre-wired electric, HDMI, digital audio & Cat 6)
- Windows are tempered glass custom made by Morvik Glazing.
- Solar qualifies for a 26% tax credit. This is not a write-off rather it is a direct reduction on your tax obligation.
- Thousands of dollars less than adding onto your home.
- Custom color, siding, features available.

This beautiful back yard office is delivered 100% assembled and ready to enjoy on the day of delivery.

We ship nationwide from our factory in South Carolina. Give us a call anytime to speak to a designer and start your dream office today!

555-318-4027
info@BriskHollowBuilders.example

```html
<!DOCTYPE html>
<html lang="en">
<head>
<meta charset="utf-8">
<title>The Cedarlane Garden Workroom – Brisk Hollow Builders</title>
<link href="https://fonts.googleapis.com/css2?family=Poppins:wght@300;400;500;600&display=swap" rel="stylesheet">
<style>
  :root {
    --green: #3f9a3c;
    --green-light: #8cc63f;
    --green-dark: #2b7a2e;
    --gold: #f2b705;
    --ink: #1d1d1b;
    --white: #ffffff;
    --brand: #d9791f;
  }
  html, body { margin: 0; padding: 0; overflow: hidden; }
  body { width: 850px; height: 1200px; background: var(--white); font-family: "Poppins", sans-serif; color: var(--ink); }
  .flyer { position: relative; width: 850px; height: 1200px; overflow: hidden; background: var(--white); }

  .hero-photo { position: absolute; left: 0; top: 0; width: 850px; height: 650px;
    background: linear-gradient(160deg, #6f8c5a 0%, #45573e 30%, #2f3a33 55%, #7c8576 80%, #a8ab9c 100%); }

  .brand-block { position: absolute; left: 0; top: 0; width: 250px; height: 165px; }
  .brand-name { position: absolute; left: 22px; top: 84px; width: 200px; margin: 0;
    font-weight: 600; font-size: 22px; line-height: 1.1; color: var(--brand); text-align: center; }
  .brand-dot { position: absolute; left: 103px; top: 34px; width: 38px; height: 38px; border-radius: 50%; background: var(--brand); }

  .headline { position: absolute; left: 28px; top: 206px; margin: 0; color: var(--white);
    font-weight: 500; font-size: 52px; line-height: 60px; letter-spacing: -0.5px;
    text-shadow: 2px 2px 3px rgba(0,0,0,0.55); }

  .photo-circle { position: absolute; border-radius: 50%; border: 7px solid var(--gold); box-sizing: border-box;
    box-shadow: 0 2px 6px rgba(0,0,0,0.3); }
  .circle-roof { left: 592px; top: 320px; width: 154px; height: 154px;
    background: linear-gradient(180deg, #9bb37a 0%, #4c5a4b 45%, #2e3530 70%, #6e8a4e 100%); }
  .circle-frame { left: 393px; top: 423px; width: 142px; height: 142px;
    background: radial-gradient(circle, #f4f4f4 0%, #dcdcdc 70%, #c8c8c8 100%); }

  .swoosh { position: absolute; left: 0; top: 560px; width: 850px; height: 120px; }

  .features-tab { position: absolute; left: 622px; top: 612px; width: 228px; height: 32px;
    background: var(--gold); border-radius: 16px 0 0 16px; margin: 0;
    font-weight: 500; font-size: 19px; line-height: 32px; padding-left: 8px; box-sizing: border-box; color: var(--ink); }

  .intro { position: absolute; left: 34px; top: 658px; width: 196px; margin: 0;
    font-weight: 300; font-size: 13px; line-height: 16px; text-align: justify; }
  .purposes { position: absolute; left: 34px; top: 978px; width: 212px; margin: 0;
    font-weight: 300; font-size: 13px; line-height: 16px; }

  .features-panel { position: absolute; left: 243px; top: 658px; width: 607px; height: 226px;
    background: linear-gradient(90deg, var(--green-light) 0%, var(--green) 55%, var(--green-dark) 100%);
    border-radius: 18px 0 0 18px; }
  .feature-list { list-style: none; margin: 0; padding: 0; position: absolute; top: 12px; }
  .feature-list.col-a { left: 14px; width: 298px; }
  .feature-list.col-b { left: 320px; width: 276px; }
  .feature-list li { position: relative; padding-left: 6px; margin-bottom: 11px; color: var(--white);
    font-weight: 500; font-size: 10.5px; line-height: 13px; }
  .feature-list li::before { content: ""; position: absolute; left: -4px; top: 2px; width: 3px; height: 8px; background: var(--gold); border-radius: 2px; }

  .delivery { position: absolute; left: 270px; top: 918px; width: 352px; margin: 0;
    font-weight: 400; font-size: 13.5px; line-height: 17px; }
  .delivery p { margin: 0 0 17px; }

  .product-thumb { position: absolute; left: 644px; top: 922px; width: 192px; height: 100px;
    background: linear-gradient(180deg, #3a3f3c 0%, #3a3f3c 18%, #d9d6cf 20%, #efece6 60%, #8c8f8a 100%); }

  .footer-band { position: absolute; left: 0; top: 1085px; width: 850px; height: 115px; }
  .contact { position: absolute; top: 1140px; display: flex; align-items: center; gap: 14px;
    color: var(--white); font-weight: 400; font-size: 23px; }
  .contact-phone { left: 56px; }
  .contact-mail { left: 380px; }
  .contact svg { width: 36px; height: 36px; }
</style>
</head>
<body>
<main class="flyer">
  <div class="hero-photo" role="img" aria-label="Photo of a dark green modern garden office with glass doors on a paved patio among trees"></div>

  <div class="brand-block">
    <svg width="250" height="165" viewBox="0 0 250 165" aria-hidden="true">
      <path d="M0 0 H250 V95 C230 150 170 165 100 162 C55 160 20 150 0 140 Z" fill="var(--white)"/>
    </svg>
    <span class="brand-dot"></span>
    <p class="brand-name">Brisk Hollow Builders</p>
  </div>

  <h1 class="headline">The<br>Cedarlane Garden<br>Workroom</h1>

  <svg class="swoosh" viewBox="0 0 850 120" preserveAspectRatio="none" aria-hidden="true">
    <path d="M0 70 C250 20 520 10 850 0 V120 H0 Z" fill="var(--green-light)"/>
    <path d="M0 88 C260 40 540 40 850 30 V120 H0 Z" fill="var(--green)"/>
    <path d="M0 100 C280 70 560 70 850 70 V120 H0 Z" fill="var(--white)"/>
  </svg>

  <div class="photo-circle circle-roof" role="img" aria-label="Photo of the workroom roof fitted with solar panels"></div>
  <div class="photo-circle circle-frame" role="img" aria-label="Illustration of the steel frame structure"></div>

  <h2 class="features-tab">Features Include:</h2>

  <p class="intro">More and more people everyday are working from home and finding it difficult to disconnect from home activities in order to focus on their work. They are also finding it very expensive to add on to their existing house for a quiet place. Our archatectually stunning, Cedarlane Garden Workroom is the answer. The office studio measures 16' wide and 10' deep. 160 Square feet of space.</p>

  <section class="features-panel">
    <ul class="feature-list col-a">
      <li>Steel Framing. 40-60% lighter then wood, higher strength to weight ratio, resistant to mold and fire and steel is the most recycled material on earth!</li>
      <li>100% Off grid with enough solar and battery storage to run your entire office. No need to pay for an expensive electric installation.</li>
      <li>Spray foam insulation. Cool in the summer and warm in the winter.</li>
      <li>HVAC Mini Split with wireless remote control and thermostat.</li>
      <li>Custom color, siding, features available</li>
    </ul>
    <ul class="feature-list col-b">
      <li>Solar qualifies for a 26% tax credit. This is not a write-off rather it is a direct reduction on your tax obligation..</li>
      <li>TV mount (Optional with pre-wired electric, HDMI, digital audio &amp; Cat 6)</li>
      <li>Windows are tempered glass custom made by Morvik Glazing.</li>
      <li>Thousands of dollars less than adding onto your home.</li>
      <li>Flush fitting floor outlets to reduce wires.</li>
    </ul>
  </section>

  <div class="delivery">
    <p>This beautiful back yard office is delivered 100% assembled and ready to enjoy on the day of delivery.</p>
    <p>We ship nationwide from our factory in South Carolina. Give us a call anytime to speak to a designer and start your dream office today!</p>
  </div>

  <div class="product-thumb" role="img" aria-label="Front view of the workroom with glass doors and windows"></div>

  <p class="purposes">Perfect for dozens of purposes. Home office, design studio, artist studio, home school office, reading room, craft studio, drafting room.</p>

  <svg class="footer-band" viewBox="0 0 850 115" preserveAspectRatio="none" aria-hidden="true">
    <path d="M0 10 C300 40 600 30 850 0 V115 H0 Z" fill="var(--green-light)"/>
    <path d="M0 28 C300 50 600 40 850 14 V115 H0 Z" fill="var(--green)"/>
  </svg>

  <div class="contact contact-phone">
    <svg viewBox="0 0 24 24" aria-hidden="true"><path d="M6.6 2.5l3 3.2-1.7 2.6c1 2.3 3.4 4.8 5.8 5.8l2.6-1.7 3.2 3-1.6 3.2c-7.6-.4-13.4-6.2-13.8-13.8z" fill="none" stroke="var(--white)" stroke-width="1.4" stroke-linejoin="round"/></svg>
    <span>555-318-4027</span>
  </div>
  <div class="contact contact-mail">
    <svg viewBox="0 0 24 24" aria-hidden="true"><rect x="3" y="7" width="18" height="13" rx="1" fill="none" stroke="var(--white)" stroke-width="1.4"/><path d="M3 8l9 7 9-7" fill="none" stroke="var(--white)" stroke-width="1.4"/><circle cx="12" cy="6" r="3" fill="none" stroke="var(--white)" stroke-width="1.2"/></svg>
    <span>info@BriskHollowBuilders.example</span>
  </div>
</main>
</body>
</html>
```